Personalized Technology Company Needs a Business Card

I need a double-sided business card. Both sides will have the logo, and the contact information. One side will be black, with the white / gray logo, and the other will be white, with the black / gray logo. The black side will have the text "Custom Gaming PC's" and will have a water-cooled gaming PC image. The white side will have the text "Custom Business Computers & Consulting", and will have a business / enterprise PC image. Feel free to add a conservative image in the background, while the color remains unchanged. I'm uploading the base logo (transparent), so you can modify the colors, both the finished colored logos and an idea of ​​the business card (with the current information, just missing the website, which is www.volinexsystems.com, please add it.) Thank you so much for your effort, I'll be specting your cool designs. Good Luck!

Target Market(s)

Gamers & Entrepreneurs / Business Owners / Chief Technology Officers

Industry/Entity Type

Technology Equipment

Contact Information for Business Card

I need a double-sided business card. Both sides will have the logo, and the contact information. One side will be black, with the white/gray logo, and the other one will be white, with the black/gray logo. The black side will have the text "Custom Gaming PC's" and will have a water-cooled gaming PC image. The white side will have the text "Custom Business Computers & Consulting", and will have a business/enterprise PC image. Feel free to add a conservative image in the background, whilst the color remains unchanged.

I'm uploading the base logo (transparent), so you can modify the colors, both the finished colored logos and an idea of the business card (with the actual information, just missing the website, which is www.volinexsystems.com, please add it.)

Thank you so much for your effort, I'll be specting your cool designs. Good Luck!

Font styles to use
Serif

Colors
000000
757575
ffffff

Requirements
Must have
• Please See Description
Nice to have
• Please See Description
Should not have
• Please See Description

```html
<!DOCTYPE html>
<html lang="en">
<head>
<meta charset="utf-8">
<title>Volinex Systems – Business Card</title>
<link href="https://fonts.googleapis.com/css2?family=Lato:ital,wght@0,400;0,700;0,900;1,400&display=swap" rel="stylesheet">
<style>
  :root {
    --backdrop: #3a3a3a;
    --card-white: #ffffff;
    --card-black: #000000;
    --ink: #111111;
    --accent-blue: #1a3fd6;
    --sand: #b5a594;
    --rule: #bdbdbd;
    --light: #ffffff;
  }
  * { margin: 0; padding: 0; box-sizing: border-box; }
  html, body { width: 1200px; height: 900px; overflow: hidden; }
  body {
    background: var(--backdrop);
    font-family: "Lato", Arial, sans-serif;
    position: relative;
  }
  .card {
    position: absolute;
    top: 170px;
    width: 347px;
    height: 561px;
    overflow: hidden;
  }
  .card--front { left: 259px; background: var(--card-white); color: var(--ink); }
  .card--back { left: 631px; background: var(--card-black); color: var(--light); }

  .brand {
    position: absolute;
    left: 0; right: 0;
    display: flex;
    align-items: center;
    justify-content: center;
    gap: 14px;
  }
  .brand__mark { width: 22px; height: 22px; border-radius: 50%; }
  .brand__name {
    font-weight: 900;
    font-size: 30px;
    letter-spacing: 4px;
    line-height: 1.05;
  }
  .card--front .brand { top: 100px; }
  .card--front .brand__mark { background: var(--ink); }
  .card--front .brand__name { color: var(--ink); }
  .card--back .brand { top: 80px; }
  .card--back .brand__mark { background: var(--sand); }
  .card--back .brand__name { color: var(--light); }

  .tagline {
    position: absolute;
    left: 0; right: 0;
    text-align: center;
  }
  .card--front .tagline {
    top: 230px;
    font-style: italic;
    font-size: 14px;
    color: var(--sand);
  }
  .card--back .tagline {
    top: 187px;
    font-size: 16px;
    letter-spacing: 0.5px;
    color: var(--light);
  }

  .person {
    position: absolute;
    top: 362px;
    left: 0; right: 0;
    text-align: center;
  }
  .person__name { font-size: 20px; color: var(--accent-blue); letter-spacing: 0.3px; }
  .person__role { font-size: 14px; margin-top: 2px; }
  .divider {
    position: absolute;
    top: 421px;
    left: 62px;
    width: 222px;
    height: 1px;
    background: var(--rule);
  }
  .contact {
    position: absolute;
    top: 438px;
    left: 0; right: 0;
    text-align: center;
    list-style: none;
    font-size: 15px;
    line-height: 20px;
  }
  .contact__label { color: var(--accent-blue); font-weight: 700; }
  .contact__web { color: var(--accent-blue); }

  .product-photo {
    position: absolute;
    left: 0;
    top: 225px;
    width: 347px;
    height: 336px;
    background:
      linear-gradient(90deg, #0d1a4a 0%, #3a6ee8 28%, #cfe0ff 45%, #2f58c9 62%, #111 72%, #1b1b1b 85%, #e9e9e9 92%, #f4f4f4 100%);
  }
</style>
</head>
<body>
  <section class="card card--front" aria-label="Business card, white side">
    <div class="brand">
      <span class="brand__mark"></span>
      <span class="brand__name">VOLINEX<br>SYSTEMS</span>
    </div>
    <p class="tagline">CUSTOM BUSINESS COMPUTERS &amp; CONSULTING</p>
    <div class="person">
      <p class="person__name">MARCO REYES LUNA</p>
      <p class="person__role">CEO &amp; Co-Founder</p>
    </div>
    <div class="divider"></div>
    <ul class="contact">
      <li><span class="contact__label">P:</span> 52 5100-2837</li>
      <li><span class="contact__label">M:</span> +52 55-4810-3364</li>
      <li><span class="contact__label">E:</span> contact@volinexsystems.com</li>
      <li class="contact__web">www.volinexsystems.com</li>
    </ul>
  </section>

  <section class="card card--back" aria-label="Business card, black side">
    <div class="brand">
      <span class="brand__mark"></span>
      <span class="brand__name">VOLINEX<br>SYSTEMS</span>
    </div>
    <p class="tagline">CUSTOM GAMING PC'S</p>
    <div class="product-photo" role="img" aria-label="Photo of a white water-cooled gaming PC case with blue lighting and glass side panel"></div>
  </section>
</body>
</html>
```